Corporate travel agency website design

Hello I need a website design that will look professional. I want that anyone that gos on our site understands that we are a large successful company. I want it to be up to par with other large companies. The site should be sleek and neat.
Below I will attach my logo. A recent one page add I made and content for my add that will be used for the website.

```html
<!DOCTYPE html>
<html lang="en">
<head>
<meta charset="utf-8">
<title>Apex Travel – Business Travel Management Services</title>
<link href="https://fonts.googleapis.com/css2?family=Montserrat:wght@400;500;600;700&display=swap" rel="stylesheet">
<style>
:root{
  --navy:#0b1e3f;
  --navy-deep:#061631;
  --ice:#d4effb;
  --mist:#f3f6fa;
  --ink:#1c2742;
  --text:#3d4a63;
  --white:#ffffff;
}
*{margin:0;padding:0;box-sizing:border-box}
html,body{width:1200px;height:4831px;overflow:hidden}
body{font-family:'Montserrat',sans-serif;color:var(--ink);background:var(--white);position:relative}
.abs{position:absolute}
.btn{position:absolute;display:flex;align-items:center;justify-content:center;font-weight:600;font-size:15px;letter-spacing:.5px;text-decoration:none}
.btn-ice{background:var(--ice);color:var(--navy)}
.btn-navy{background:var(--navy);color:var(--white)}
.eyebrow{position:absolute;font-size:15px;font-weight:500;text-transform:uppercase;letter-spacing:.5px}
.heading{position:absolute;font-weight:600;text-transform:uppercase;letter-spacing:.5px;line-height:1.18}
.copy{position:absolute;font-size:13.4px;line-height:21.2px;color:var(--text)}
.copy p+p{margin-top:16px}
.photo{position:absolute}

/* hero */
.hero{position:absolute;left:0;top:0;width:1200px;height:622px;overflow:hidden}
.hero .photo{left:0;top:0;width:1200px;height:622px;background:linear-gradient(90deg,#06183a 0%,#0b2248 35%,#51607a 55%,#a3acb9 75%,#d6dbe2 100%)}
.brand{position:absolute;display:flex;align-items:center;gap:10px;color:var(--white);font-weight:600}
.brand .dot{width:12px;height:12px;border-radius:50%;background:currentColor;flex:none}
.brand .name{font-size:20px;white-space:nowrap}
.nav{position:absolute;top:42px;font-size:14px;color:var(--white)}
.hero-title{position:absolute;left:110px;top:252px;font-size:55px;font-weight:600;line-height:59px;color:var(--white)}
.corner{position:absolute;width:26px;height:26px;border-color:var(--white);border-style:solid}

/* why */
.why-tab{left:1121px;top:622px;width:79px;height:231px;background:var(--ice);display:flex;flex-direction:column;align-items:center;justify-content:center;font-weight:700;font-size:14px;line-height:18px}
.travel-band{left:0;top:1162px;width:941px;height:408px;background:linear-gradient(100deg,#161c22 0%,#2f3538 35%,#6b6852 62%,#c8b98a 78%,#4a4a40 100%)}
.ghost{position:absolute;font-weight:700;color:rgba(255,255,255,.22);letter-spacing:4px}

/* service */
.globe-map{left:0;top:1890px;width:760px;height:270px;background:radial-gradient(ellipse at 45% 40%,#e3f1fb 0%,#f2f8fd 55%,rgba(255,255,255,0) 80%)}
.jet{left:600px;top:1945px;width:488px;height:118px;background:radial-gradient(ellipse at 50% 50%,#c7cfdc 0%,#e9edf3 55%,rgba(255,255,255,0) 75%)}

/* budget */
.budget{left:0;top:2160px;width:1200px;height:859px;background:var(--mist)}

/* efficiency */
.eff-photo{left:0;top:3019px;width:1033px;height:600px;background:linear-gradient(90deg,#2a2d33 0%,#3e3f43 30%,#1a2a48 55%,#0b1e3f 75%,#0b1e3f 100%)}

/* partner */
.partner{left:0;top:3619px;width:1200px;height:1046px;background:linear-gradient(180deg,#ffffff 0%,#eaf4fb 30%,#f4f8fb 60%,#ffffff 100%)}
.node-label{position:absolute;font-size:16px;font-weight:600;line-height:23px;text-transform:uppercase;color:var(--ink)}

/* footer */
.footer{left:0;top:4665px;width:1200px;height:166px;background:var(--navy-deep)}
</style>
</head>
<body>

<!-- HERO -->
<header class="hero">
  <div class="photo" role="img" aria-label="Businessman in a grey suit walking through an airport terminal with a phone and rolling suitcase"></div>
  <div class="brand" style="left:150px;top:112px">
    <span class="dot"></span>
    <span class="name">Apex Travel</span>
  </div>
  <nav>
    <a class="nav" style="left:600px">Home</a>
    <a class="nav" style="left:702px">About</a>
    <a class="nav" style="left:805px">Services</a>
  </nav>
  <a class="btn btn-ice" style="left:920px;top:32px;width:149px;height:41px">CONTACT US</a>
  <div class="corner" style="left:86px;top:238px;border-width:4px 0 0 4px"></div>
  <h1 class="hero-title">Business Travel<br>Management<br>Services</h1>
  <div class="corner" style="left:518px;top:405px;border-width:0 4px 4px 0"></div>
  <a class="btn btn-ice" style="left:110px;top:478px;width:147px;height:40px">CONTACT US</a>
</header>

<!-- WHY -->
<section class="why">
  <div class="abs why-tab"><span>W</span><span>H</span><span>Y</span></div>
  <div class="eyebrow" style="left:233px;top:726px">Why choose</div>
  <h2 class="heading" style="left:233px;top:755px;font-size:39px">Apex Travel?</h2>
  <div class="abs" style="left:0;top:853px;width:234px;height:231px;background:var(--ice)"></div>
  <div class="copy" style="left:352px;top:856px;width:592px">
    <p>Apex Travel is a global leader in business travel management services. We drive savings, efficiency, and unparalleled service to businesses and their travelers all around the world. If you are looking for a tailored travel managed solution focused on offering white glove service and fulfilling your individual preferences ,while delivering customer excellence, you've come to the right place.</p>
    <p>At Apex Travel, our mission is to have you focus on your day to day business while we handle all of the logistics and details for the most successful all encompassing travel experience. From emergency passport arrangements to last minute cancellations, re-bookings, and other intricate travel challenges, Apex Travel is well versed in handling the routine array of travel services, as well as solving any travel related issue that might arise.</p>
  </div>
</section>

<!-- TRAVEL BAND -->
<section>
  <div class="photo travel-band" role="img" aria-label="Airplane cabin interior with seats and a sunlit window"></div>
  <div class="ghost" style="left:4px;top:1455px;font-size:118px;line-height:1">TRAVEL</div>
  <svg class="abs" style="left:770px;top:1200px" width="340" height="340" viewBox="0 0 340 340">
    <circle cx="168" cy="169" r="165" fill="var(--navy)"/>
    <circle cx="168" cy="169" r="140" fill="var(--ice)"/>
    <path d="M60 115 A118 118 0 0 1 276 115" fill="none" stroke="var(--navy)" stroke-width="2"/>
    <path d="M276 223 A118 118 0 0 1 60 223" fill="none" stroke="var(--navy)" stroke-width="2"/>
    <path d="M45 210 A128 128 0 0 1 45 128" fill="none" stroke="var(--white)" stroke-width="2.5"/>
    <path d="M40 142 L45 128 L52 141" fill="none" stroke="var(--white)" stroke-width="2.5"/>
    <path d="M291 128 A128 128 0 0 1 291 210" fill="none" stroke="var(--white)" stroke-width="2.5"/>
    <path d="M284 197 L291 210 L297 196" fill="none" stroke="var(--white)" stroke-width="2.5"/>
    <line x1="28" y1="169" x2="308" y2="169" stroke="var(--navy)" stroke-width="5"/>
    <circle cx="168" cy="169" r="42" fill="var(--white)" stroke="var(--navy)" stroke-width="2"/>
    <text x="168" y="101" text-anchor="middle" font-family="Montserrat,sans-serif" font-size="14" font-weight="600" fill="var(--navy)">High quality services</text>
    <text x="168" y="245" text-anchor="middle" font-family="Montserrat,sans-serif" font-size="14" font-weight="600" fill="var(--navy)">Satisfied customers</text>
  </svg>
</section>

<!-- SERVICE -->
<section>
  <div class="photo globe-map" role="img" aria-label="Faint dotted world map"></div>
  <div class="eyebrow" style="left:0;width:1200px;top:1690px;text-align:center">We prowide</div>
  <h2 class="heading" style="left:0;width:1200px;top:1722px;text-align:center;font-size:41px">Unparalleled Service</h2>
  <p class="copy" style="left:252px;top:1799px;width:718px;text-align:center;color:var(--ink)"><b>Apex Travel</b> is famous for our concierge style approach to travel. From detailed planning, to commercial or private air travel, transportation, including car rentals, chauffers, busses for larger groups, hotels, all styles of lodging accomodations, special event planning and more, Apex Travel is like having your own personal or corporate travel butler.</p>
  <a class="btn btn-navy" style="left:536px;top:1920px;width:148px;height:40px">CONTACT US</a>
  <div class="photo jet" role="img" aria-label="Passenger jet in flight"></div>
</section>

<!-- BUDGET -->
<section>
  <div class="abs budget"></div>
  <div class="eyebrow" style="left:233px;top:2254px">You'll get</div>
  <h2 class="heading" style="left:233px;top:2280px;font-size:40px;line-height:50px">Budget and<br>travel spend<br>reporting</h2>
  <p class="copy" style="left:233px;top:2461px;width:330px">Having a <b style="color:var(--ink)">travel management service</b> will ensure that your company enforces corporate compliance and maintains control over travel decisions. This ensures that your employees stick to your budget, which in turn will protect your bottom line. Travel expenses can be costly.</p>
  <div class="photo" style="left:662px;top:2240px;width:538px;height:361px;background:linear-gradient(135deg,#7c958a 0%,#a9bcb2 40%,#c7d2cc 70%,#8fa299 100%)" role="img" aria-label="Hands holding a tablet showing a world map chart beside printed reports"></div>
  <div class="photo" style="left:234px;top:2681px;width:368px;height:244px;background:linear-gradient(135deg,#cfd6e0 0%,#a4b0c2 45%,#6e7a8a 100%)" role="img" aria-label="Desk with charts, a tablet and hands holding a wallet"></div>
  <p class="copy" style="left:662px;top:2671px;width:306px">Having a savvy and experienced corporate travel manager who can access deep discounts not available to the public will ensure your travel is booked across the board at the lowest prices expenses are kept under control. Travel reporting is critical to optimizing budgets, streamlining expense reports, and recognizing key trends. Apex Travel customizes travel spend reports, by team, project, department etc, so companies can accurately track travel expenses, and make critical decisions based on the spend.</p>
</section>

<!-- EFFICIENCY -->
<section>
  <div class="photo eff-photo" role="img" aria-label="Smiling businessman seated in an airport lounge"></div>
  <div class="abs" style="left:1024px;top:3178px;width:15px;height:291px;background:var(--ice)"></div>
  <div class="eyebrow" style="left:529px;top:3128px;color:var(--white)">Our value</div>
  <h2 class="heading" style="left:529px;top:3158px;font-size:39px;color:var(--white)">Efficiency</h2>
  <div class="abs" style="left:548px;top:3234px;width:1px;height:141px;background:var(--white)"></div>
  <p class="copy" style="left:570px;top:3231px;width:372px;color:#e6ecf5">Having a savvy and experienced corporate travel manager who can access deep discounts not available to the public will ensure your travel is booked across the board at the lowest prices expenses are kept under control. Travel reporting is critical to optimizing budgets, streamlining expense reports, and recognizing key trends. Apex Travel customizes travel spend reports, by team, project, department etc, so companies can accurately track travel expenses, and make critical decisions based on the spend.</p>
  <div class="corner" style="left:938px;top:3459px;border-width:0 4px 4px 0"></div>
</section>

<!-- PARTNER -->
<section>
  <div class="abs partner" role="img" aria-label="Soft sky with light clouds"></div>
  <h2 class="heading" style="left:0;width:1200px;top:3754px;text-align:center;font-size:41px">Apex Travel</h2>
  <p class="abs" style="left:0;width:1200px;top:3820px;text-align:center;font-size:16px;line-height:23px;font-weight:500">WE'RE YOUR CORPORATE TRAVEL PARTNER TO HELP YOU<br>MANAGE IT ALL.</p>
  <svg class="abs" style="left:300px;top:3860px" width="600" height="400" viewBox="300 3860 600 400">
    <g stroke="var(--navy)" stroke-width="6" fill="none">
      <path d="M428 3932 L470 3945 L530 4010"/>
      <path d="M428 4073 L470 4060 L530 4045"/>
      <path d="M782 3932 L730 3945 L670 4010"/>
      <path d="M782 4073 L730 4060 L670 4045"/>
      <path d="M600 4115 L600 4134"/>
    </g>
    <g fill="var(--white)" stroke="var(--navy)" stroke-width="2.5">
      <circle cx="381" cy="3932" r="46"/>
      <circle cx="381" cy="4073" r="46"/>
      <circle cx="829" cy="3932" r="46"/>
      <circle cx="829" cy="4073" r="46"/>
      <circle cx="600" cy="4181" r="46"/>
    </g>
    <circle cx="600" cy="4031" r="84" fill="#f7f8fa" stroke="#e2e6ec" stroke-width="2"/>
    <g fill="none" stroke="var(--navy)" stroke-width="2">
      <path d="M370 3950 L370 3925 M377 3948 L377 3918 M384 3948 L384 3920 M391 3948 L391 3926 M370 3950 Q380 3958 392 3948"/>
      <path d="M362 4080 L398 4064 L402 4068 L368 4086 Z M378 4072 L372 4062 M384 4070 L392 4082"/>
      <circle cx="829" cy="3932" r="14"/><ellipse cx="829" cy="3932" rx="6" ry="14"/><line x1="815" y1="3932" x2="843" y2="3932"/>
      <rect x="818" y="4058" width="20" height="28" rx="2"/><circle cx="828" cy="4068" r="5"/><circle cx="815" cy="4083" r="6"/>
      <rect x="588" y="4166" width="20" height="26"/><rect x="593" y="4171" width="20" height="26" fill="var(--white)"/>
    </g>
  </svg>
  <div class="node-label" style="left:120px;width:197px;top:3908px;text-align:right">White glove<br>service</div>
  <div class="node-label" style="left:120px;width:197px;top:4045px;text-align:right">Corporate<br>travel policy<br>compliance</div>
  <div class="node-label" style="left:894px;top:3908px">Unparalleled<br>savings</div>
  <div class="node-label" style="left:894px;top:4045px">Full service<br>travel<br>management</div>
  <div class="node-label" style="left:0;width:1200px;top:4238px;text-align:center">Streamlined<br>expense reports</div>
  <div class="ghost" style="left:0;width:1200px;top:4392px;text-align:center;font-size:100px;line-height:1;color:rgba(11,30,63,.05)">APEX TRAVEL</div>
  <div class="photo" style="left:160px;top:4350px;width:928px;height:272px;background:radial-gradient(ellipse at 50% 55%,#3a3f48 0%,#9aa1ab 30%,rgba(230,234,240,.6) 55%,rgba(255,255,255,0) 72%)" role="img" aria-label="Front view of a jet airliner in flight"></div>
</section>

<!-- FOOTER -->
<footer>
  <div class="abs footer"></div>
  <div class="brand" style="left:150px;top:4740px">
    <span class="dot"></span>
    <span class="name" style="font-size:17px">Apex Travel</span>
  </div>
  <p class="abs" style="left:0;width:1200px;top:4750px;text-align:center;font-size:11px;color:var(--white)">©Copyright 2023. Apex Travel | All Rights Reserved</p>
  <svg class="abs" style="left:880px;top:4741px" width="142" height="32" viewBox="0 0 142 32">
    <g fill="none" stroke="var(--white)" stroke-width="1.5">
      <circle cx="16" cy="16" r="13"/><circle cx="52" cy="16" r="13"/><circle cx="88" cy="16" r="13"/><circle cx="125" cy="16" r="13"/>
    </g>
  </svg>
</footer>

</body>
</html>
```